Aerial photo/video drone company needs new business card

Aerial visual company who offers photos and video services via drones.

We are QVL certified and work in the real estate, insurance, construction, and film industries.

I'm looking for a clean, professional, maybe even edgy design, that will be a conversation starter when networking.

I've included our logo, current business card, and font.

Our current business card is decent; albeit, I'm looking for something more unique. If you folks provide good designs, I'll definitely guarantee payment (and I'm not opposed to tipping if the design is above and beyond).

Target Market(s)

Insurance companies, real estate agents, construction companies, advertising & other creative agencies, and filmmakers/producers.

Industry/Entity Type

Business

Contact Information for Business Card

Company name pronounced air-a-vee.

Font styles to use
Other font styles liked:
• Font was uploaded; that or similar; not opposed to other fonts if they work well with the design

Requirements
Must have
• Clearly prominent logo; my name and title; phone number; email address; web address; mentioned "QVL Certified" or similar; should indicate "Aerial visual"
Nice to have
• Watermark of logo or otherwise
Should not have
• Pictures of drones or scenic shots

```html
<!DOCTYPE html>
<html lang="en">
<head>
<meta charset="utf-8">
<title>Skyloft Business Card</title>
<link rel="stylesheet" href="https://fonts.googleapis.com/css2?family=Montserrat:wght@500;600;700&display=swap">
<style>
  :root {
    --brand-blue: #2196d6;
    --brand-navy: #233a5e;
    --card-white: #ffffff;
    --backdrop: #1c1c1e;
  }
  * { margin: 0; padding: 0; box-sizing: border-box; }
  html, body {
    width: 1200px; height: 900px; overflow: hidden;
    background: var(--backdrop);
    font-family: "Montserrat", sans-serif;
  }
  .canvas {
    position: relative; width: 1200px; height: 900px;
    display: flex; flex-direction: column; align-items: center; justify-content: center; gap: 30px;
  }
  .card {
    position: relative; width: 700px; height: 400px; overflow: hidden;
    box-shadow: 0 10px 30px rgba(0,0,0,.5);
  }
  /* front */
  .card-front {
    background: var(--brand-blue);
    display: flex; align-items: center; justify-content: center; gap: 22px;
  }
  .front-dot { width: 34px; height: 34px; border-radius: 50%; background: var(--card-white); }
  .front-wordmark {
    color: var(--card-white); font-weight: 600; font-size: 104px; letter-spacing: 1px; line-height: 1;
  }
  /* back */
  .card-back { background: var(--card-white); }
  .back-shapes { position: absolute; inset: 0; }
  .back-wordmark {
    position: absolute; right: 80px; top: 58px;
    color: var(--brand-navy); font-weight: 600; font-size: 56px; line-height: 1;
  }
  .contact-block { position: absolute; left: 118px; top: 128px; color: var(--brand-navy); }
  .holder-name { color: var(--brand-blue); font-weight: 700; font-size: 29px; line-height: 1.1; }
  .holder-title { font-weight: 500; font-size: 18px; margin-top: 4px; }
  .contact-list { list-style: none; margin-top: 16px; }
  .contact-item { display: flex; align-items: center; gap: 10px; font-weight: 500; font-size: 20px; height: 30px; }
  .contact-icon { width: 22px; height: 22px; flex: none; }
  .service-line { font-weight: 500; font-size: 17px; margin-top: 22px; }
  .cert-line { font-weight: 600; font-size: 18px; margin-top: 8px; }
</style>
</head>
<body>
<main class="canvas">
  <section class="card card-front" aria-label="Card front">
    <span class="front-dot"></span>
    <span class="front-wordmark">skyloft</span>
  </section>

  <section class="card card-back" aria-label="Card back">
    <svg class="back-shapes" viewBox="0 0 700 400" aria-hidden="true">
      <polygon points="0,120 110,120 40,330 0,330" fill="var(--brand-navy)"/>
      <polygon points="0,330 40,330 0,400" fill="var(--brand-blue)"/>
      <polygon points="620,0 700,0 700,150" fill="var(--brand-blue)"/>
      <polygon points="688,0 700,0 700,400 688,400" fill="var(--brand-navy)"/>
      <polygon points="540,400 688,190 688,400" fill="var(--brand-blue)"/>
    </svg>

    <div class="back-wordmark">skyloft</div>

    <div class="contact-block">
      <h1 class="holder-name">Daniel J. Morrow</h1>
      <p class="holder-title">Owner - sUAS Pilot</p>
      <ul class="contact-list">
        <li class="contact-item">
          <svg class="contact-icon" viewBox="0 0 24 24"><circle cx="12" cy="12" r="12" fill="var(--brand-blue)"/><path d="M8 6.5l2 0 1 3-1.5 1a7 7 0 0 0 4 4l1-1.5 3 1v2a1.5 1.5 0 0 1-1.5 1.5A10 10 0 0 1 6.5 8 1.5 1.5 0 0 1 8 6.5z" fill="#fff"/></svg>
          415.300.7721
        </li>
        <li class="contact-item">
          <svg class="contact-icon" viewBox="0 0 24 24"><circle cx="12" cy="12" r="12" fill="var(--brand-blue)"/><rect x="6" y="8" width="12" height="8" fill="none" stroke="#fff" stroke-width="1.5"/><path d="M6 8l6 5 6-5" fill="none" stroke="#fff" stroke-width="1.5"/></svg>
          dan@skyloft.com
        </li>
        <li class="contact-item">
          <svg class="contact-icon" viewBox="0 0 24 24"><circle cx="12" cy="12" r="12" fill="var(--brand-blue)"/><circle cx="12" cy="12" r="6" fill="none" stroke="#fff" stroke-width="1.5"/><ellipse cx="12" cy="12" rx="2.6" ry="6" fill="none" stroke="#fff" stroke-width="1.3"/><path d="M6 12h12" stroke="#fff" stroke-width="1.3"/></svg>
          www.skyloft.com
        </li>
      </ul>
      <p class="service-line">Aerial Visual for Real Estate | Insurance | Construction | Film</p>
      <p class="cert-line">QVL Part 107 Commercial sUAS Certified</p>
    </div>
  </section>
</main>
</body>
</html>
```